Marlow Creek sign

24"x36" sign for new home construction job site. Located in affluent in-town neighborhood in Midwest. Traditional american style homes. 2nd generation construction company. Sign needs to convey strength and elegance but not overly elaborate. Competition most has signs consisting of text.

Sign text reads:
Marlow Creek Builders
Custom Luxury for Over 20 years
248-555-0137

Target Market(s)

Upper middle income home buyers

Industry/Entity Type

Construction

Font styles to use
Serif
Decorative

Requirements
Must have
• Logo image no more than 2 colors
Nice to have
• Should be visible and legible from distance of 30'
Should not have
• Not just image of house as logo

```html
<!DOCTYPE html>
<html lang="en">
<head>
<meta charset="utf-8">
<title>Marlow Creek Builders — Job Site Sign</title>
<link href="https://fonts.googleapis.com/css2?family=Roboto+Condensed:wght@300;400;700&display=swap" rel="stylesheet">
<style>
  :root {
    --brand-red: #a7181e;
    --frame-red: #b01c22;
    --paper: #ffffff;
    --slate: #6d6e71;
    --swoosh: #9a9b9e;
  }
  html, body {
    margin: 0;
    padding: 0;
    width: 1200px;
    height: 900px;
    overflow: hidden;
    background: var(--paper);
  }
  .sign {
    position: relative;
    width: 1200px;
    height: 900px;
    font-family: "Roboto Condensed", "Arial Narrow", sans-serif;
  }
  .sign-frame {
    position: absolute;
    inset: 0;
  }
  .tagline {
    position: absolute;
    left: 109px;
    width: 1008px;
    text-align: center;
    color: var(--paper);
    margin: 0;
  }
  .tagline-lead {
    top: 128px;
    font-weight: 300;
    font-size: 86px;
    line-height: 1;
    letter-spacing: 0.5px;
  }
  .tagline-years {
    top: 228px;
    font-weight: 700;
    line-height: 1;
  }
  .tagline-years .years-number {
    font-size: 104px;
  }
  .tagline-years .years-word {
    font-size: 76px;
    margin-left: 8px;
  }
  .company-name {
    position: absolute;
    left: 109px;
    width: 1008px;
    text-align: center;
    color: var(--brand-red);
    font-weight: 400;
    margin: 0;
  }
  .company-name-main {
    top: 440px;
    font-size: 128px;
    line-height: 1;
    letter-spacing: 10px;
  }
  .company-name-sub {
    top: 565px;
    font-size: 54px;
    line-height: 1;
    letter-spacing: 62px;
    padding-left: 62px;
  }
  .phone {
    position: absolute;
    left: 109px;
    width: 1008px;
    top: 660px;
    text-align: center;
    color: var(--slate);
    font-weight: 700;
    font-size: 112px;
    line-height: 1;
    letter-spacing: 12px;
    margin: 0;
  }
</style>
</head>
<body>
  <main class="sign">
    <svg class="sign-frame" width="1200" height="900" viewBox="0 0 1200 900" aria-hidden="true">
      <rect class="outer-border" x="86" y="86" width="1060" height="704" fill="none" stroke="var(--frame-red)" stroke-width="10"/>
      <rect class="inner-border" x="101" y="101" width="1024" height="674" fill="none" stroke="var(--frame-red)" stroke-width="5"/>
      <path class="headline-swoosh" d="M109 318 Q 613 392 1117 332 L1117 346 Q 613 404 109 330 Z" fill="var(--swoosh)"/>
      <path class="headline-band" d="M109 109 H1117 V332 Q 613 388 109 318 Z" fill="var(--brand-red)"/>
      <g class="rating-stars" fill="var(--paper)" stroke="var(--swoosh)" stroke-width="1.5">
        <polygon points="558,372 561,380 569,380 563,385 565,393 558,388 551,393 553,385 547,380 555,380"/>
        <polygon points="585,372 588,380 596,380 590,385 592,393 585,388 578,393 580,385 574,380 582,380"/>
        <polygon points="613,368 617,378 628,378 619,384 622,395 613,389 604,395 607,384 598,378 609,378"/>
        <polygon points="641,372 644,380 652,380 646,385 648,393 641,388 634,393 636,385 630,380 638,380"/>
        <polygon points="668,372 671,380 679,380 673,385 675,393 668,388 661,393 663,385 657,380 665,380"/>
      </g>
      <line class="phone-rule" x1="109" y1="645" x2="1117" y2="645" stroke="var(--frame-red)" stroke-width="3"/>
    </svg>

    <p class="tagline tagline-lead">Custom Luxury for Over</p>
    <p class="tagline tagline-years"><span class="years-number">20</span><span class="years-word">YEARS</span></p>

    <p class="company-name company-name-main">MARLOW CREEK</p>
    <p class="company-name company-name-sub">BUILDERS</p>

    <p class="phone">248-555-0137</p>
  </main>
</body>
</html>
```